Create a Graphic About YOURSELF and PixelHarbor

PixelHarbor would like you (designers) to create an awesome graphic to promote YOURSELF and your profile on PixelHarbor!

Your graphic should communicate your name, your services and should mention PixelHarbor.

The design should be perfect for sharing on Chatterly. Here's an example of what we'd like http://blog.pixelharbor-example.ca/article/333/pixelharbor-launches-3000-hire-me-social-design-contest

Once you submitted your design, we'd love you to share the design ('advertisement') and promote yourself and PixelHarbor to your friends and potential customers. So make your submissions great and get your friends to vote for your design by 'Liking' it on Chatterly!

Prizes:
$1500 - "PixelHarbor Community" prize awarded to the designer with the most Chatterly 'Likes'
5 x $50 for the next 5 'most liked' designs on Chatterly

$1000 - "Hire Me" prize awarded to the designer who receives the most client invites
5 x $50 for the next 5 'most invited' designers

In summary, this is a great opportunity for you to increase your exposure to PixelHarbor customers and win cash prizes. Show off your design skills and get hired by PixelHarbor customers from around the world!

Target Market(s)

Fans, friends and customers of YOU

Industry/Entity Type

Cash

Requirements
Must have
• 1) Include your PixelHarbor user name on the graphic so customers can find you in the PixelHarbor Designer Directory
2) Include the tagline "Hire Me on PixelHarbor.com!" in your graphic design.
3) Share your design's URL on our Chatterly wall at http://chatterly-example.com/pixelharbor and get your friends to 'like' your design.
Nice to have
• 1) Include a tagline that expresses your design approach/philosophy
2) Artwork dimensions: 403 x 403 px
3) You can submit more than 1 design!
Should not have
• You must own the copyright of any images you use including stock imagery.

```html
<!DOCTYPE html>
<html lang="en">
<head>
<meta charset="utf-8">
<title>Kavro – Creative Designer</title>
<link href="https://fonts.googleapis.com/css2?family=Dosis:wght@400;500&family=Source+Sans+3:wght@400&display=swap" rel="stylesheet">
<style>
  :root {
    --bg-dark: #262626;
    --bg-light: #2c2c2c;
    --accent-yellow: #ffe500;
    --text-white: #f2f2f2;
    --text-dark: #1f1f1f;
    --portrait-light: #e9e9e9;
    --portrait-dark: #3a3a3a;
  }
  html, body {
    margin: 0;
    padding: 0;
    overflow: hidden;
    background: var(--bg-dark);
  }
  .promo-card {
    position: relative;
    width: 1194px;
    height: 1200px;
    overflow: hidden;
    background: radial-gradient(ellipse at 40% 35%, var(--bg-light), var(--bg-dark) 75%);
  }
  .designer-name {
    position: absolute;
    left: 108px;
    top: 228px;
    margin: 0;
    font-family: "Dosis", sans-serif;
    font-weight: 400;
    font-size: 196px;
    line-height: 1;
    letter-spacing: 16px;
    color: var(--accent-yellow);
  }
  .designer-role {
    position: absolute;
    left: 100px;
    top: 478px;
    margin: 0;
    font-family: "Dosis", sans-serif;
    font-weight: 400;
    font-size: 68px;
    line-height: 1;
    letter-spacing: 7px;
    color: var(--text-white);
  }
  .portrait-area {
    position: absolute;
    left: 806px;
    top: 284px;
    width: 226px;
    height: 537px;
    border-radius: 40% 30% 20% 45% / 25% 25% 30% 30%;
    background: linear-gradient(160deg, var(--portrait-light) 0%, #bdbdbd 55%, var(--portrait-dark) 100%);
  }
  .hire-banner {
    position: absolute;
    left: 0;
    top: 1116px;
    width: 1194px;
    height: 84px;
  }
  .hire-banner-shape { fill: var(--accent-yellow); }
  .hire-banner-text {
    position: absolute;
    left: 524px;
    top: 1130px;
    margin: 0;
    font-family: "Source Sans 3", sans-serif;
    font-weight: 400;
    font-size: 43px;
    line-height: 1.2;
    color: var(--text-dark);
  }
</style>
</head>
<body>
  <main class="promo-card">
    <h1 class="designer-name">KAVRO</h1>
    <p class="designer-role">CREATIVE DESIGNER</p>
    <div class="portrait-area" role="img" aria-label="High-contrast white silhouette portrait of the designer"></div>
    <svg class="hire-banner" viewBox="0 0 1194 84" aria-hidden="true">
      <polygon class="hire-banner-shape" points="494,0 1194,0 1194,84 470,84"/>
    </svg>
    <p class="hire-banner-text">hire me on pixelharbor.com</p>
  </main>
</body>
</html>
```